Exciting New Reseller Brand requires Website to WOW New clients to register.

We are a NEW online business called Trade Our Goods.

The Website is a simple concept, it looks to put Merchants (businesses that want their products resold) in touch with Resellers (people or businesses that want to resell that product).

The website acts as an online market place which looks to get Merchants to sign-up and pay to list their company and product as well as getting Resellers to sign-up to view potential Merchants they can get in touch with in the right industry or area to resell their products for (see attached slide-pack to explain packages)

Any type of Industry or Business can register themselves to get listed on Trade Our Goods to see either get their product/service resold or to look for products / services to reseller.

Trade Our Goods does not take any other monetary part in the business relationships other than to obtain money for the monthly website subscription.

We want a very simple website, so this project is for several pages:

Page 1) A really vibrant, exciting, image based homepage to get people to sign-up / register (see sites that we like in the project brief). Needs to be very clear that there are 2 customers and to sign up to join, build and earn!

Page 2) A page that describes the benefits and packages for Resellers.

Page 3) A page that describes the benefits and packages for Merchants.

Page 4) The Payment process pages, taking the customer through sign-up

Page 5) The Business Listings page, so when people search for a Merchant how this will be displayed.

We would really like an image based site and preferably parallax. We want it bright vibrant and to look like a social media site.

All necessary files / logos enclosed.

We would love to continue to work with the winning designer moving forward.

Many thanks and Good Luck.

Regards

Martin & Owen

Target Market(s)

Merchants, Suppliers, Vendors, Manufacturers, Distributors, Wholesalers, Affiliate programs, Franchisees, Reselers

Industry/Entity Type

Business

Number of Pages Required

5+ page

Requirements
Must have
• We love the following websites:
• 1) Like the top section, i.e. parallax image based: www.brightkitestudio.co.uk
• 2) Like the way the screen is split in 2, could be used to describe the 2 different customers we are after Merchants / Resellers: www.filevault-example.com/guide
• 3) Like the bright colours / full screen video split into 2 below top banner and the generally how simple the site is: www.harbourlinden.com.au
• 4) Love all of this site, simple, bold, Love the colours, the clear message and the infographics: http://www.velorin-example.com/swiftrider/faster

```html
<!DOCTYPE html>
<html lang="en">
<head>
<meta charset="utf-8">
<title>Trade Our Goods – Join · Build · Earn</title>
<link href="https://fonts.googleapis.com/css2?family=Open+Sans:wght@400;600;700;800&family=Raleway:wght@300;400;600&display=swap" rel="stylesheet">
<style>
:root{
  --blue:#2f8fd6;
  --blue-dark:#1f76bb;
  --green:#8dc63f;
  --green-dark:#76ad2c;
  --ink:#333333;
  --muted:#777777;
  --light:#f3f3f3;
  --dark:#2b2b2b;
  --footer:#3b3b3b;
  --footer-bottom:#2a2a2a;
  --teal:#26b0c9;
  --white:#ffffff;
}
*{box-sizing:border-box;margin:0;padding:0}
html,body{width:1200px;height:3296px;overflow:hidden}
body{font-family:"Open Sans",Arial,sans-serif;color:var(--ink);background:var(--white)}

/* HERO */
.hero{position:relative;height:584px;overflow:hidden}
.hero-photo{position:absolute;inset:0;background:linear-gradient(110deg,#cfd6d9 0%,#b7c4c8 35%,#8fa3a8 60%,#c9cfcf 100%)}
.hero-shade{position:absolute;inset:0;background:rgba(40,50,55,.35)}
.nav{position:absolute;top:0;left:0;right:0;height:104px;display:flex;align-items:center;justify-content:space-between;padding:0 60px 0 108px}
.brand{display:flex;align-items:center;gap:12px;color:var(--white);font-weight:700;font-size:26px;letter-spacing:.2px}
.brand-dot{width:30px;height:30px;border-radius:50%;background:var(--teal)}
.nav-links{display:flex;gap:38px;list-style:none}
.nav-links li{color:var(--white);font-size:13px;font-weight:600;letter-spacing:1px}
.hero-copy{position:absolute;top:262px;left:0;right:0;text-align:center;color:var(--white)}
.hero-kicker{font-family:"Raleway",sans-serif;font-weight:400;font-size:34px;letter-spacing:3px;text-transform:uppercase}
.hero-title{font-family:"Raleway",sans-serif;font-weight:600;font-size:58px;letter-spacing:8px;margin-top:8px}
.scroll-down{position:absolute;left:580px;top:488px;width:40px;height:40px}

/* SPLIT */
.split{display:flex;height:304px}
.split-side{flex:1;color:var(--white);text-align:center;padding-top:34px}
.split-side.merchants{background:var(--blue)}
.split-side.resellers{background:var(--green)}
.split-title{font-size:44px;font-weight:800;letter-spacing:1px;line-height:1}
.split-sub{font-size:24px;font-weight:600;margin-top:8px}
.split-body{font-size:13px;line-height:20px;width:480px;margin:18px auto 0;opacity:.95}
.split-btn{display:inline-block;margin-top:22px;background:var(--white);font-size:11px;font-weight:700;letter-spacing:1px;padding:7px 26px;border-radius:2px}
.merchants .split-btn{color:var(--blue)}
.resellers .split-btn{color:var(--green-dark)}

/* MISSION */
.mission{height:384px;background:var(--light);text-align:center;padding-top:74px}
.mission-title{font-size:48px;font-weight:600;color:#3a3a3a;line-height:58px}
.mission-title em{font-style:normal;color:var(--green)}
.mission-text{width:860px;margin:30px auto 0;font-size:15px;line-height:26px;color:var(--muted)}

/* BENEFITS */
.benefits{position:relative;height:408px;overflow:hidden}
.benefits-photo{position:absolute;inset:0;background:linear-gradient(90deg,#3c3c3c,#595959 40%,#474747 70%,#2f2f2f)}
.benefits-shade{position:absolute;inset:0;background:rgba(20,20,20,.45)}
.benefits-inner{position:relative;text-align:center;color:var(--white);padding-top:100px}
.benefits-title{font-size:52px;font-weight:600;letter-spacing:1px}
.benefits-actions{display:flex;justify-content:center;gap:40px;margin-top:50px}
.outline-btn{width:236px;height:74px;border:3px solid var(--white);display:flex;align-items:center;justify-content:center;font-size:26px;font-weight:600;letter-spacing:1px}

/* BLOG */
.blog{height:1160px;padding-top:40px;text-align:center}
.blog-title{font-size:48px;font-weight:600;color:#3a3a3a}
.blog-grid{display:flex;gap:18px;padding:0 33px;margin-top:38px;text-align:left;align-items:flex-start}
.blog-col{width:270px;display:flex;flex-direction:column;gap:20px}
.post{background:var(--white);box-shadow:0 1px 4px rgba(0,0,0,.18);position:relative}
.post-media{display:block;width:100%}
.post-date{position:absolute;top:12px;left:12px;width:42px;background:var(--blue);color:var(--white);text-align:center;padding:5px 0;line-height:1}
.post-date b{display:block;font-size:20px}
.post-date span{font-size:10px;font-weight:600}
.post-body{padding:16px 18px 14px}
.post-title{font-size:19px;font-weight:600;color:#333;line-height:24px}
.post-excerpt{font-size:12px;line-height:18px;color:var(--muted);margin-top:8px}
.post-more{font-size:11px;font-weight:700;color:#333;margin-top:10px}
.post-meta{font-size:10px;color:#aaa;margin-top:6px;padding-top:8px;border-top:1px solid #eee}
.load-more{margin:32px auto 0;width:150px;font-size:11px;letter-spacing:1px;color:var(--muted);text-align:center}

/* CTA */
.cta{position:relative;height:200px;overflow:hidden}
.cta-photo{position:absolute;inset:0;background:linear-gradient(90deg,#9aa7ad,#c7cfd2 50%,#a3aeb3)}
.cta-box{position:absolute;left:96px;top:38px;width:1008px;height:112px;background:var(--teal);border:4px solid rgba(255,255,255,.8);display:flex;align-items:center;justify-content:center;color:var(--white);font-size:38px;font-weight:700;letter-spacing:.5px}

/* FOOTER */
.footer{height:232px;background:var(--footer);color:#cfcfcf;display:flex;padding:40px 0 0 112px}
.footer-brand{width:330px}
.footer-brand .brand{font-size:22px}
.footer-contact{width:260px;font-size:11px;line-height:18px}
.social{display:flex;gap:12px;margin-top:20px}
.social i{width:20px;height:20px;border-radius:50%;background:#8a8a8a;display:block}
.footer-list{width:210px}
.footer-list h4{font-size:12px;color:var(--white);letter-spacing:1px;margin-bottom:10px}
.footer-list li{list-style:none;font-size:11px;line-height:20px;border-bottom:1px solid #4a4a4a}
.copyright{height:24px;background:var(--footer-bottom);color:#888;font-size:10px;line-height:24px;padding-left:112px}
</style>
</head>
<body>

<header class="hero">
  <div class="hero-photo" role="img" aria-label="Photo of a smiling businesswoman at her desk holding documents, bright office behind her"></div>
  <div class="hero-shade"></div>
  <nav class="nav">
    <div class="brand"><span class="brand-dot"></span>Trade Our Goods</div>
    <ul class="nav-links">
      <li>HOME</li><li>MERCHANTS</li><li>RESELLERS</li><li>BLOG</li><li>FAQS</li><li>CONTACT</li>
    </ul>
  </nav>
  <div class="hero-copy">
    <p class="hero-kicker">Buildng You Own Virtual Sales Team</p>
    <h1 class="hero-title">JOIN · BUILD · EARN</h1>
  </div>
  <svg class="scroll-down" viewBox="0 0 40 40"><circle cx="20" cy="20" r="19" fill="rgba(255,255,255,.35)"/><path d="M12 15l8 8 8-8M12 21l8 8 8-8" stroke="#fff" stroke-width="2.5" fill="none"/></svg>
</header>

<section class="split">
  <div class="split-side merchants">
    <h2 class="split-title">MERCHANTS</h2>
    <p class="split-sub">Register To Build Your Virtual Sales Team</p>
    <p class="split-body">Reach motivated sellers across every industry and let a growing network of resellers take your products to new customers while you focus on running your business.</p>
    <span class="split-btn">BUILD</span>
  </div>
  <div class="split-side resellers">
    <h2 class="split-title">RESELLERS</h2>
    <p class="split-sub">Register To Start Earning Money</p>
    <p class="split-body">Browse trusted merchants in your area or field, choose the products you believe in and start building a steady income by reselling them to your own contacts.</p>
    <span class="split-btn">EARN</span>
  </div>
</section>

<section class="mission">
  <h2 class="mission-title">Bringing Reseller Opportunities<br>to the <em>masses.</em></h2>
  <p class="mission-text">Trade Our Goods brings merchants and resellers together in one simple marketplace. Merchants list their products and services, resellers find the right partners in their industry or area, and both sides grow their reach. Join today, build your network and start to earn.</p>
</section>

<section class="benefits">
  <div class="benefits-photo" role="img" aria-label="Photo of business people in suits meeting around a table"></div>
  <div class="benefits-shade"></div>
  <div class="benefits-inner">
    <h2 class="benefits-title">BENEFITS FOR EVERYONE</h2>
    <div class="benefits-actions">
      <span class="outline-btn">MERCHANTS</span>
      <span class="outline-btn">RESELLERS</span>
    </div>
  </div>
</section>

<section class="blog">
  <h2 class="blog-title">Helping Businesses &amp; Resellers</h2>
  <div class="blog-grid">
    <div class="blog-col">
      <article class="post">
        <svg class="post-media" height="208" role="img" aria-label="Photo of stacked business cards on a wooden desk"><rect width="100%" height="100%" fill="#c9b9a3"/></svg>
        <div class="post-date"><b>29</b><span>Mar</span></div>
        <div class="post-body"><h3 class="post-title">Modern business cards</h3><p class="post-excerpt">Clean layouts and bold type help a small card leave a lasting first impression.</p><p class="post-more">Read More ›</p><p class="post-meta">By Admin · 2 Comments</p></div>
      </article>
      <article class="post">
        <svg class="post-media" height="172" role="img" aria-label="Illustration of two smartphones showing a weather app"><rect width="100%" height="100%" fill="#7a5fa8"/></svg>
        <div class="post-body"><h3 class="post-title">Weather mobile app</h3><p class="post-excerpt">A bright forecast app showing the week ahead at a single glance.</p><p class="post-more">Read More ›</p><p class="post-meta">By Admin · 2 Comments</p></div>
      </article>
    </div>
    <div class="blog-col">
      <article class="post">
        <svg class="post-media" height="300" role="img" aria-label="Photo of a hand holding a smartphone with a music app"><rect width="100%" height="100%" fill="#a8b6c2"/></svg>
        <div class="post-date"><b>26</b><span>Mar</span></div>
        <div class="post-body"><h3 class="post-title">Mobile music app</h3><p class="post-excerpt">A simple player with clear controls that lets listeners find their music fast.</p><p class="post-more">Read More ›</p><p class="post-meta">By Admin · 2 Comments</p></div>
      </article>
      <article class="post">
        <svg class="post-media" height="168" role="img" aria-label="Photo of dark textured business cards"><rect width="100%" height="100%" fill="#3f4246"/></svg>
        <div class="post-date"><b>22</b><span>Mar</span></div>
        <div class="post-body"><h3 class="post-title">Business cards design trends</h3><p class="post-excerpt">Textured paper, spot colour and rounded corners are back on the desk this year.</p><p class="post-more">Read More ›</p><p class="post-meta">By Admin · 2 Comments</p></div>
      </article>
    </div>
    <div class="blog-col">
      <article class="post">
        <svg class="post-media" height="172" role="img" aria-label="Photo of a dark card with subtle embossing"><rect width="100%" height="100%" fill="#55595e"/></svg>
        <div class="post-date"><b>18</b><span>Mar</span></div>
        <div class="post-body"><h3 class="post-title">Frozen emotions</h3><p class="post-excerpt">Quiet colours and soft light set the mood for this calm photo series.</p><p class="post-more">Read More ›</p><p class="post-meta">By Admin · 2 Comments</p></div>
      </article>
      <article class="post">
        <svg class="post-media" height="300" role="img" aria-label="Photo of a hand holding a smartphone with a music app"><rect width="100%" height="100%" fill="#b4bcc4"/></svg>
        <div class="post-date"><b>15</b><span>Mar</span></div>
        <div class="post-body"><h3 class="post-title">Mobile music app</h3><p class="post-excerpt">A second take on the player with playlists and a darker night theme.</p><p class="post-more">Read More ›</p><p class="post-meta">By Admin · 2 Comments</p></div>
      </article>
    </div>
    <div class="blog-col">
      <article class="post">
        <svg class="post-media" height="164" role="img" aria-label="Photo grid of a creative team at work"><rect width="100%" height="100%" fill="#9db3c4"/></svg>
        <div class="post-date"><b>12</b><span>Mar</span></div>
        <div class="post-body"><h3 class="post-title">How to choose a perfect creative agency</h3><p class="post-excerpt">Look at past work, ask about process and agree on clear goals before you start.</p><p class="post-more">Read More ›</p><p class="post-meta">By Admin · 2 Comments</p></div>
      </article>
      <article class="post">
        <svg class="post-media" height="216" role="img" aria-label="Photo of a lit suspension bridge at dusk"><rect width="100%" height="100%" fill="#3d6b96"/></svg>
        <div class="post-body"><h3 class="post-title">Most beautiful world bridges</h3><p class="post-excerpt">A tour of famous crossings that join cities, rivers and coastlines around the world.</p><p class="post-more">Read More ›</p><p class="post-meta">By Admin · 2 Comments</p></div>
      </article>
    </div>
  </div>
  <p class="load-more">LOAD MORE</p>
</section>

<section class="cta">
  <div class="cta-photo" role="img" aria-label="Faded photo of business people shaking hands"></div>
  <div class="cta-box">FIND YOUR IDEAL BUSINESS PARTNER MATCH NOW</div>
</section>

<footer class="footer">
  <div class="footer-brand"><div class="brand"><span class="brand-dot"></span>Trade Our Goods</div></div>
  <div class="footer-contact">
    Trade Our Goods Ltd<br>12 Market Street<br>Northgate, Leeds<br>LS1 4AB<br>Phone: 0113 555 0192<br>hello@tradeourgoods.example
    <div class="social"><i></i><i></i><i></i><i></i><i></i></div>
  </div>
  <div class="footer-list">
    <h4>RECENT POSTS</h4>
    <ul><li>Modern business cards</li><li>Mobile music app</li><li>Frozen emotions</li><li>Weather mobile app</li><li>Business card trends</li></ul>
  </div>
  <div class="footer-list" style="margin-left:30px">
    <h4>POPULAR POSTS</h4>
    <ul><li>Most beautiful bridges</li><li>Choosing a creative agency</li><li>Mobile music app</li><li>Modern business cards</li><li>Frozen emotions</li></ul>
  </div>
</footer>
<div class="copyright">© 2015 Trade Our Goods. All rights reserved.</div>

</body>
</html>
```